Geschäftspapiere
Zielgruppe
Wir sind ein Fachpflegedienst für außerklinische Intensivpflege. Unsere Zielgruppe sind Patienten, Angehörige, Krankenkassen und Kliniken
Aufgabenstellung
Wir benötigen ein ansprechendes Briefpapier. Das Design soll zu unserer Webseite und unserer Broschüre passen. Die Webseite ist www.lunovera-pflege.de und die Broschüre ist im Anhang. Wichtig ist, dass die Badges auf dem Briefpapier zu sehen sind.

```html
<!DOCTYPE html>
<html lang="de">
<head>
<meta charset="utf-8">
<title>Lunovera Briefpapier</title>
<link rel="stylesheet" href="https://fonts.googleapis.com/css2?family=Roboto:ital,wght@0,400;0,700;1,400&display=swap">
<style>
  :root {
    --canvas: #ffffff;
    --paper: #e8eef8;
    --brand-blue: #2b4b8f;
    --brand-red: #d3292c;
    --rule: #ecaaab;
    --text: #1d1d1f;
    --badge-dark: #3a3d44;
    --badge-navy: #2e3a78;
    --badge-blue: #3f7fd0;
    --badge-light: #f4f6fa;
    --signature: #c9cfdc;
  }
  * { box-sizing: border-box; margin: 0; padding: 0; }
  html, body {
    width: 1200px; height: 1200px; overflow: hidden;
    background: var(--canvas);
    font-family: "Roboto", Arial, sans-serif;
  }
  .letterhead {
    position: absolute; left: 211px; top: 50px;
    width: 778px; height: 1100px;
    background: var(--paper);
  }
  .brand {
    position: absolute; left: 77px; top: 88px;
    display: flex; align-items: center; gap: 8px;
  }
  .brand-dot {
    width: 14px; height: 14px; border-radius: 50%;
    background: var(--brand-blue);
  }
  .brand-name {
    font-size: 19px; font-weight: 700; letter-spacing: 0.5px;
    color: var(--brand-blue);
  }
  .badges {
    position: absolute; left: 470px; top: 70px;
    display: flex; align-items: center; gap: 22px;
    height: 48px;
  }
  .badge-seal { width: 48px; height: 48px; border-radius: 50%; background: var(--badge-dark); }
  .badge-card { width: 35px; height: 47px; background: var(--badge-navy); border: 2px solid var(--badge-light); outline: 1px solid #9aa3b8; }
  .badge-ring { width: 46px; height: 46px; border-radius: 50%; background: var(--badge-light); border: 2px solid var(--badge-blue); }
  .badge-rating { width: 44px; height: 24px; border-radius: 4px; background: #cfd8ea; }
  .writing-lines {
    position: absolute; left: 112px; top: 297px; width: 554px;
  }
  .writing-line {
    position: absolute; left: 0; height: 1px; background: var(--rule);
  }
  .sender {
    position: absolute; left: 77px; top: 920px;
  }
  .sender-name { font-size: 17.5px; font-weight: 700; color: var(--brand-red); white-space: nowrap; }
  .sender-role { font-size: 13.5px; font-style: italic; color: var(--brand-red); margin-top: 3px; }
  .signature {
    position: absolute; left: 77px; top: 974px; width: 100px; height: 66px;
    background: linear-gradient(120deg, var(--signature), rgba(201,207,220,0.3));
    border-radius: 4px;
  }
  .contacts {
    position: absolute; right: 95px; top: 966px;
    list-style: none;
  }
  .contact {
    display: flex; align-items: center; justify-content: flex-end; gap: 12px;
    height: 21px; font-size: 11.5px; color: var(--text);
  }
  .contact-icon { width: 17px; height: 17px; flex: none; order: 0; }
  .contact-text { white-space: nowrap; text-align: right; min-width: 140px; }
</style>
</head>
<body>
<main class="letterhead">
  <header>
    <div class="brand">
      <span class="brand-dot"></span>
      <span class="brand-name">LUNOVERA</span>
    </div>
    <div class="badges" aria-label="Auszeichnungen">
      <span class="badge-seal"></span>
      <span class="badge-card"></span>
      <span class="badge-ring"></span>
      <span class="badge-rating"></span>
    </div>
  </header>

  <section class="writing-lines" aria-hidden="true">
    <span class="writing-line" style="top:0;width:554px"></span>
    <span class="writing-line" style="top:54px;width:554px"></span>
    <span class="writing-line" style="top:107px;width:554px"></span>
    <span class="writing-line" style="top:161px;width:554px"></span>
    <span class="writing-line" style="top:215px;width:554px"></span>
    <span class="writing-line" style="top:268px;width:554px"></span>
    <span class="writing-line" style="top:322px;width:554px"></span>
    <span class="writing-line" style="top:376px;width:554px"></span>
    <span class="writing-line" style="top:430px;width:554px"></span>
    <span class="writing-line" style="top:483px;width:288px"></span>
  </section>

  <footer>
    <div class="sender">
      <p class="sender-name">Jonas Bergmann LL.M.</p>
      <p class="sender-role">Geschäftsführer</p>
    </div>
    <div class="signature" role="img" aria-label="Handschriftliche Unterschrift des Geschäftsführers"></div>

    <ul class="contacts">
      <li class="contact">
        <svg class="contact-icon" viewBox="0 0 18 18"><circle cx="9" cy="9" r="8" fill="none" stroke="var(--brand-red)" stroke-width="1.2"/><path d="M6.2 5.2l1.4-.3.8 1.9-.9.7c.5 1.1 1.3 1.9 2.4 2.4l.7-.9 1.9.8-.3 1.4c-3.4.2-6.2-2.6-6-6z" fill="none" stroke="var(--brand-red)" stroke-width="1"/></svg>
        <span class="contact-text">(07000) - 482 19 30</span>
      </li>
      <li class="contact">
        <svg class="contact-icon" viewBox="0 0 18 18"><circle cx="9" cy="9" r="8" fill="none" stroke="var(--brand-red)" stroke-width="1.2"/><rect x="5.5" y="6.5" width="7" height="5" rx="0.6" fill="var(--brand-red)"/><path d="M5.8 6.9L9 9.3l3.2-2.4" fill="none" stroke="var(--paper)" stroke-width="0.8"/></svg>
        <span class="contact-text">info@lunovera-pflege.de</span>
      </li>
      <li class="contact">
        <svg class="contact-icon" viewBox="0 0 18 18"><circle cx="9" cy="9" r="8" fill="none" stroke="var(--brand-red)" stroke-width="1.2"/><rect x="5.5" y="6" width="2.2" height="6.5" fill="var(--brand-red)"/><rect x="8.3" y="5" width="4.2" height="7.5" fill="var(--brand-red)"/><rect x="9.2" y="6.2" width="2.4" height="1.2" fill="var(--paper)"/></svg>
        <span class="contact-text">(07000) - 482 19 32</span>
      </li>
    </ul>
  </footer>
</main>
</body>
</html>
```